Brennick Setter Club - Rare dog breed club needs web design!

The Transylvanian Hound (or Erdélyi kopó) is an ancient Hungarian dog breed. These medium-sized hounds were favored by the Hungarian kings and princes for hunting bears and wolves in the Carpathian mountains of Transylvania. The breed's great adaptability to the region's extreme climates of sweltering summers and frigid winters made it an excellent all season hunting dog. This dog has a sleek appearance and stunning good looks. They are lean, appear very elegant and proud. Their erect posture and beautifully sculpted head portray great attentiveness and authority. In general, this rare breed is extremely good natured, loyal and obedient. It has a tendency to form strong attachments to its primary caretakers and will remain loyal and protective. (Please refer to existing web resources.)

The Brennick Setter Club - with current website www.brennicksetter.com - is the official breed club of Transylvanian Hound afficionados, breeders and owners in the United States, which was founded in 2010. We are looking for a web design for the new, upgraded version of this central (currenty non-functioning) website. Please do not recycle the old logo (we may choose from your suggesions and pay for it!) or any of the old texts. Please use the structure described below. Overall, the webpage serves a dual purpose: an educational one (about the breed itself) and a community-building one (inside the Club). The proposed structure of the website is as follows:

1. About the Kopó
- Breed History
- Breed Standard
- Public Education
- Photo Gallery

2. Life with a Kopó
- Health and Genetics
- Feeding and Nutrition
- Training and Activities

3. Finding a Kopó
- Is this the Right Breed for You?
- Choosing a Puppy
- FAQ
- Breeder Referral

4. The Brennick Setter Club
- Constituton
- Officers and Appointees
- Code of Ethics
- Breeder Guidelines
- Membership
- Reports
- Links

5. News and Events

6. Shop

We are attaching a couple of examples of the graphics/drawings of the dogs that would be part of the design of the website. We plan to have more of these artistic depictions, nicely embedded into the background (maybe shaded out at the edges just like the drawings themselves) and less actual photos. Or a good combination of the two.

Further information upon request.

Reason: There are a few very promising design collaborations ongoing. As we moved the brief to a more artistic and graphic direction, we felt that one week of extension would be needed to get to the perfect end-product, which could include designs for sub-pages as well.

Reason: In order to make the final modifications to the leading designs, and at the request of those designers, the deadline is extended until Friday.

Target Market(s)

- BRSC Club members, dog (especially T-Hound) owners, past and future owners, breeders, puppy buyers, hunters, kennel clubs, dog show participants, vets, animal shelters, Hungarian, Romanian and other European web visitors, historians

Industry/Entity Type

Club

Font styles to use
Serif
Decorative
Script

Requirements
Must have
• - Sync with graphics of dogs (see attachments), but accentuate the rich black basic color of the dogs
- Elegance, aristocratic/noble look and feel (but not overly archaic)
- Love, companionship, dogs as family members
- Hunting usage, but no bloody associations, rather romantic ones
- Simple to use and navigate for non-web-natives
- Old world (Central European) atmosphere, even the exotic, rustic and romantic Transylvanian feel - SEE the new attachment for inspiration (this was a design plan which we discarded (mainly because of its gothic, (nazi-like), unreadable font, and the fact that the plan makes the black-looking dogs appear brown), however we loved the fact that it was not full of boxes/windows, had a marble/sand stone like continuous background, lots of little elegant graphics, the drawings embedded, etc.
Nice to have
• - Working on smartphone, Zentabs, etc., so dynamic website design
- Web shop to be added to functionalities in the future (?)
- English language for now, in the future can be Hungarian, Romanian, etc., so the font choice should handle various alphabets
- Focus on the dogs (likely more graphics than photos, at least on the main pages), and not on the activities/humans - the design should accentuate the black and not the tan of the graphics!
Should not have
• - Old logo from the old www.brennicksetter.com webpage or the other logo from the Chatterly site of the Brennick Setter Club, we will have a new one (maybe designed by you!)
- Breed club, kennel club cliches
- Cutesy, adorable, cheesy design elements
- Old, stale, monolithic, archaic, snobbish, etc. look and feel
- No vampire associations

```html
<!DOCTYPE html>
<html lang="en">
<head>
<meta charset="utf-8">
<title>Brennick Setter Club – About the Kopó</title>
<link href="https://fonts.googleapis.com/css2?family=Josefin+Sans:wght@300;400&family=Herr+Von+Muellerhoff&display=swap" rel="stylesheet">
<style>
  :root {
    --paper: #efe9e8;
    --ink: #2b2726;
    --text: #6e6866;
    --text-soft: #8b8482;
    --rule: #d9d2d0;
    --dots: #8f8886;
    --parchment: #f4edd4;
    --parchment-edge: #e7dcb8;
    --hound-dark: #35302c;
    --hound-tan: #8a5a3a;
    --icon: #4a4544;
  }
  * { box-sizing: border-box; margin: 0; padding: 0; }
  html, body { width: 1200px; height: 1172px; overflow: hidden; }
  body {
    position: relative;
    background: radial-gradient(ellipse at 50% 40%, #f3eeed 0%, var(--paper) 70%, #e8e1e0 100%);
    font-family: "Josefin Sans", sans-serif;
    font-weight: 300;
    color: var(--text);
  }
  .abs { position: absolute; }

  /* header */
  .brand {
    left: 470px; top: 52px; width: 220px;
    font-size: 18px; letter-spacing: 0.5px; line-height: 18px;
    color: var(--ink); text-transform: uppercase; text-align: center;
  }
  .nav-rule { height: 0; border-top: 2px dotted var(--dots); }
  .nav-rule.top { left: 204px; top: 146px; width: 796px; }
  .nav-rule.bottom { left: 254px; top: 206px; width: 698px; }
  .laurel {
    top: 142px; width: 72px; height: 84px;
    background: linear-gradient(160deg, #7d7674, #5e5856);
    opacity: 0.55; border-radius: 50% 10% 50% 10%;
  }
  .laurel.left { left: 154px; }
  .laurel.right { left: 970px; transform: scaleX(-1); }
  .main-nav {
    left: 225px; top: 169px; width: 740px;
    display: flex; align-items: center; justify-content: space-between;
    font-size: 14px; color: var(--text);
  }
  .main-nav a { color: inherit; text-decoration: none; }
  .nav-mark {
    display: inline-block; width: 16px; height: 16px;
    background: var(--icon); border-radius: 3px; opacity: 0.8;
  }

  /* intro */
  .page-title {
    left: 158px; top: 252px;
    font-family: "Herr Von Muellerhoff", cursive;
    font-size: 82px; color: var(--ink); white-space: nowrap;
  }
  .quote-mark { font-family: Georgia, serif; font-size: 28px; color: var(--ink); }
  .quote-mark.open { left: 592px; top: 242px; }
  .quote-mark.close { left: 1026px; top: 340px; }
  .intro {
    left: 627px; top: 251px; width: 392px;
    font-size: 13.4px; line-height: 16px; color: var(--text);
  }

  /* hound illustration: narrow at the head so it stays clear of the right column text */
  .hound {
    left: 527px; top: 386px; width: 222px; height: 438px;
    background: linear-gradient(170deg, #4a3d33 0%, var(--hound-dark) 45%, #2f2a27 70%, var(--hound-tan) 100%);
    clip-path: polygon(8% 0, 62% 0, 62% 50%, 100% 62%, 100% 100%, 0 100%, 0 12%);
    opacity: 0.9;
    z-index: 0;
  }

  /* rules */
  .rule { height: 0; border-top: 1px solid var(--rule); }

  /* sections */
  .section-title {
    font-family: "Herr Von Muellerhoff", cursive;
    font-size: 40px; color: var(--ink); line-height: 40px; white-space: nowrap;
    z-index: 1;
  }
  .section-text {
    width: 333px; font-size: 9.6px; line-height: 12px; color: var(--text-soft);
    text-align: justify; z-index: 1;
  }
  .read-more {
    font-size: 10px; color: var(--text-soft); font-style: italic;
    text-decoration: underline; display: flex; align-items: center; gap: 5px;
    z-index: 1;
  }
  .read-more .nav-mark { width: 14px; height: 12px; }

  /* basic info card */
  .info-card {
    left: 708px; top: 594px; width: 353px; height: 230px;
    background: radial-gradient(ellipse at 40% 40%, #f8f2de 0%, var(--parchment) 60%, var(--parchment-edge) 100%);
    box-shadow: 0 0 6px rgba(160,140,110,0.35);
    z-index: 2;
  }
  .info-list { font-size: 9.8px; line-height: 12px; color: var(--text-soft); list-style: none; }
  .info-list b { font-weight: 400; color: var(--ink); }

  /* gallery */
  .photo {
    top: 883px; width: 150px; height: 142px; border-radius: 50%;
    background: radial-gradient(circle at 50% 50%, #3b3230 0%, #5b4a3e 45%, #8d7f78 70%, rgba(200,190,188,0) 76%);
  }
  .photo.muted { opacity: 0.75; }

  /* footer */
  .footer-rule { top: 1105px; height: 0; border-top: 2px dotted var(--dots); }
  .footer-mark {
    left: 582px; top: 1090px; width: 48px; height: 34px;
    background: #d8c4c4; border-radius: 40%; opacity: 0.6;
  }
  .footer-note { left: 113px; top: 1126px; font-size: 10px; line-height: 12px; color: var(--text-soft); }
  .social-links {
    right: 138px; top: 1132px;
    display: flex; align-items: center; gap: 14px;
  }
  .social {
    display: flex; align-items: center; gap: 5px;
    font-size: 10px; color: var(--icon); text-decoration: none;
  }
  .social i { width: 9px; height: 9px; border-radius: 50%; background: var(--icon); display: inline-block; flex: none; }
</style>
</head>
<body>

<header>
  <div class="abs brand">Brennick Setter<br>Club</div>
  <div class="abs nav-rule top"></div>
  <div class="abs laurel left" role="img" aria-label="Laurel branch ornament"></div>
  <nav class="abs main-nav">
    <a href="#">About the Kopó</a><span class="nav-mark" role="img" aria-label="Hound silhouette"></span>
    <a href="#">Life with a Kopó</a><span class="nav-mark" role="img" aria-label="Hound silhouette"></span>
    <a href="#">Finding a Kopó</a><span class="nav-mark" role="img" aria-label="Hound silhouette"></span>
    <a href="#">The Brennick Setter Club</a><span class="nav-mark" role="img" aria-label="Hound silhouette"></span>
    <a href="#">News &amp; Events</a><span class="nav-mark" role="img" aria-label="Hound silhouette"></span>
    <a href="#">Shop</a>
  </nav>
  <div class="abs laurel right" role="img" aria-label="Laurel branch ornament"></div>
  <div class="abs nav-rule bottom"></div>
</header>

<main>
  <h1 class="abs page-title">About the Kopó</h1>
  <span class="abs quote-mark open">“</span>
  <p class="abs intro">Introduction paragraph on Transylvanian Hounds. Lorem ipsum dolor sit amet, consectetur adipisicing elit, sed do eiusmod tempor incididunt ut labore et dolore magna aliqua. Ut enim ad minim veniam, quis nostrud exercitation ullamco laboris nisi ut aliquip ex ea commodo consequat. Duis aute irure dolor in reprehenderit in voluptate velit esse cillum dolore eu fugiat nulla pariatur. Excep-</p>
  <span class="abs quote-mark close">”</span>

  <div class="abs rule" style="left:152px; top:431px; width:905px;"></div>
  <div class="abs rule" style="left:152px; top:597px; width:356px;"></div>
  <div class="abs rule" style="left:692px; top:597px; width:365px;"></div>
  <div class="abs rule" style="left:152px; top:772px; width:356px;"></div>

  <div class="abs hound" role="img" aria-label="Painted illustration of a seated black and tan Transylvanian Hound"></div>

  <section>
    <h2 class="abs section-title" style="left:165px; top:447px;">Breed History</h2>
    <p class="abs section-text" style="left:175px; top:496px;">Lorem ipsum dolor sit amet, consectetur adipisicing elit, sed do eiusmod tempor incididunt ut labore et dolore magna aliqua. Ut enim ad minim veniam, quis nostrud exercitation ullamco laboris nisi ut aliquip ex ea commodo consequat. Duis aute irure dolor in reprehenderit in voluptate velit esse cillum dolore eu fugiat nulla pariatur. Excepteur sint occaecat cupidatat</p>
    <a class="abs read-more" style="left:438px; top:566px;" href="#"><span class="nav-mark" role="img" aria-label="Hound silhouette"></span>Read More</a>
  </section>

  <section>
    <h2 class="abs section-title" style="left:688px; top:447px;">Breed Standards</h2>
    <p class="abs section-text" style="left:692px; top:496px;">Lorem ipsum dolor sit amet, consectetur adipisicing elit, sed do eiusmod tempor incididunt ut labore et dolore magna aliqua. Ut enim ad minim veniam, quis nostrud exercitation ullamco laboris nisi ut aliquip ex ea commodo consequat. Duis aute irure dolor in reprehenderit in voluptate velit esse cillum dolore eu fugiat nulla pariatur. Excepteur sint occaecat cupidatat</p>
    <a class="abs read-more" style="left:953px; top:566px;" href="#"><span class="nav-mark" role="img" aria-label="Hound silhouette"></span>Read More</a>
  </section>

  <section>
    <h2 class="abs section-title" style="left:165px; top:620px;">Public Education</h2>
    <p class="abs section-text" style="left:175px; top:665px;">Lorem ipsum dolor sit amet, consectetur adipisicing elit, sed do eiusmod tempor incididunt ut labore et dolore magna aliqua. Ut enim ad minim veniam, quis nostrud exercitation ullamco laboris nisi ut aliquip ex ea commodo consequat. Duis aute irure dolor in reprehenderit in voluptate velit esse cillum dolore eu fugiat nulla pariatur. Excepteur sint occaecat cupidatat</p>
    <a class="abs read-more" style="left:438px; top:735px;" href="#"><span class="nav-mark" role="img" aria-label="Hound silhouette"></span>Read More</a>
  </section>

  <aside class="abs info-card">
    <h2 class="abs section-title" style="left:36px; top:20px;">Basic Info</h2>
    <ul class="abs info-list" style="left:61px; top:62px; width:265px;">
      <li><b>Name:</b> Transylvanian Hound</li>
      <li><b>Other names:</b> Erdélyi kopó, Transylvanischer Laufhund, Ungarische Bracke, Copoi ardelenesc, Transylvanian Blood-hound, Hungarian Hound, Transylvanian Scenthound</li>
      <li><b>Origin:</b> Hungary</li>
      <li><b>Life span:</b> 10 to 12 years</li>
      <li><b>Temperament:</b> Courageous, Protective, Good-natured, Loyal</li>
    </ul>
    <ul class="abs info-list" style="left:155px; top:162px; width:180px;">
      <li><b>Weight:</b> 66-77 pounds (30-35 kg)</li>
      <li><b>Height:</b> 18-21 inches (46-53 cm)</li>
      <li><b>Colors:</b> Black &amp; Tan</li>
    </ul>
  </aside>

  <section>
    <h2 class="abs section-title" style="left:165px; top:805px;">Photo Gallery</h2>
    <div class="abs photo muted" style="left:183px;" role="img" aria-label="Photo of two black and tan hounds"></div>
    <div class="abs photo" style="left:408px;" role="img" aria-label="Close-up photo of a black and tan hound"></div>
    <div class="abs photo muted" style="left:637px;" role="img" aria-label="Photo of two black and tan hounds"></div>
    <div class="abs photo muted" style="left:867px;" role="img" aria-label="Close-up photo of a black and tan hound"></div>
    <a class="abs read-more" style="left:972px; top:1060px;" href="#"><span class="nav-mark" role="img" aria-label="Hound silhouette"></span>See All</a>
  </section>
</main>

<footer>
  <div class="abs footer-rule" style="left:112px; width:462px;"></div>
  <div class="abs footer-mark" role="img" aria-label="Faint hound drawing"></div>
  <div class="abs footer-rule" style="left:642px; width:419px;"></div>
  <p class="abs footer-note">Brennick Setter Club<br>Est. 2010</p>
  <div class="abs social-links">
    <a class="social" href="#"><i></i>Chirpline</a>
    <a class="social" href="#"><i></i>Chatterly</a>
  </div>
</footer>

</body>
</html>
```